Belle Journée Weddings and Events

I am a small boutique wedding coordinator, stylist and bridal consultant/coach/assistant. I am based in Brisbane, Australia and my business is geared towards mid range- high end budget bridal couples.
I am after some business cards that are double sided, with the logo on one side and all other information on the other side, including the business tagline of design, create, celebrate. The look of the card needs to be clean and crisp, with white and the tones of grey of the logo.The final design needs to convey sophistication and poise. Perhaps the logo and tagline could be done in a metallic silver with the rest of the text in the shades of grey from the style guide attached below.
Title- Mirela Tostavanque - Director / Events Manager and Stylist
Address - 218 Hollis Terrace, Marwick Vale, QLD, 4067
Phone- 07 3482 9517
Mobile- 0418 572 906
Email- Mirela@bellejourneeevents.com.au
Website- www.bellejourneeevents.com.au

```html
<!DOCTYPE html>
<html lang="en">
<head>
<meta charset="utf-8">
<title>Belle Journée Weddings and Events — Business Card</title>
<link rel="stylesheet" href="https://fonts.googleapis.com/css2?family=Mulish:wght@300;400;700&display=swap">
<style>
  :root {
    --backdrop: #ececec;
    --card-dark: #1c1c1d;
    --card-light: #2b2b2c;
    --silver: #b9b9bb;
    --grey-soft: #8e8e90;
    --grey-mid: #a6a6a8;
    --white: #f4f4f4;
    --ornament: #3a3a3c;
  }
  * { box-sizing: border-box; margin: 0; padding: 0; }
  html, body {
    width: 1200px; height: 720px; overflow: hidden;
    background: var(--backdrop);
    font-family: "Mulish", "Century Gothic", sans-serif;
  }
  .canvas {
    position: relative; width: 1200px; height: 720px;
    display: flex; justify-content: center; align-items: center; gap: 62px;
  }
  .card {
    width: 480px; height: 274px;
    background: linear-gradient(160deg, var(--card-light) 0%, var(--card-dark) 65%);
    position: relative;
    display: flex; flex-direction: column; align-items: center;
  }
  /* Front */
  .card-front { justify-content: flex-start; }
  .brand {
    margin-top: 86px;
    text-align: center;
    color: var(--silver);
    font-weight: 300;
  }
  .brand-name { display: block; font-size: 40px; letter-spacing: 0.5px; line-height: 1; }
  .brand-sub { display: block; font-size: 11px; letter-spacing: 0.6px; margin-top: 8px; }
  .front-tagline {
    position: absolute; bottom: 30px; left: 0; right: 0;
    text-align: center; font-size: 11px; font-weight: 400;
    color: var(--grey-mid); letter-spacing: 0.3px;
  }
  /* Back */
  .card-back { padding-top: 34px; text-align: center; }
  .ornament { width: 112px; height: 24px; display: block; }
  .person-name { margin-top: 6px; font-size: 21px; font-weight: 700; color: var(--white); letter-spacing: 0.3px; }
  .person-role { margin-top: 3px; font-size: 10.5px; color: var(--grey-mid); }
  .contact { margin-top: 16px; font-size: 13px; color: var(--white); line-height: 1.3; font-weight: 400; }
  .contact + .contact { margin-top: 12px; }
  .website {
    position: absolute; bottom: 22px; left: 0; right: 0;
    font-size: 13px; color: var(--grey-soft); letter-spacing: 0.3px;
  }
  .website strong { font-weight: 700; }
</style>
</head>
<body>
  <main class="canvas">
    <section class="card card-front" aria-label="Card front">
      <div class="brand">
        <span class="brand-name">Belle Journée</span>
        <span class="brand-sub">Weddings and Events</span>
      </div>
      <p class="front-tagline">Wedding Coordinator, Stylist and Bridal Consultant/Coach/Assistant</p>
    </section>

    <section class="card card-back" aria-label="Card back">
      <svg class="ornament" viewBox="0 0 112 24" role="img" aria-label="Decorative scroll flourish">
        <rect x="0" y="4" width="112" height="16" rx="8" fill="var(--ornament)"/>
      </svg>
      <h1 class="person-name">Mirela Tostavanque</h1>
      <p class="person-role">Director / Events Manager and Stylist</p>
      <p class="contact">Phone: 07 3482 9517<br>Mobile: 0418 572 906</p>
      <p class="contact">Email: Mirela@bellejourneeevents.com.au</p>
      <p class="contact">218 Hollis Terrace, Marwick Vale, QLD, 4067</p>
      <p class="website">www.<strong>bellejourneeevents</strong>.com.au</p>
    </section>
  </main>
</body>
</html>
```